Business Card Design Project

- makeup artist business card

- original and creative

- Elegant design

- Feel free to come out with cool designs but stick to being elegant and attractive

- Design relates to makeup

- includes name, occupation, contact numbers, email, website

- regular size business card

- round corner card

- double sided

- on 1 side it should just have the website name in the center " browsandblush.example "

Industry/Entity Type

Business

Requirements
Must have
• Marla Voss
Makeup Artist
USA: +1 (415)872-6410
Singapore: +65 83027715
marlavoss@browsandblush.example
www.browsandblush.example
Should not have
• nothing cartoon looking.
Pictures of makeup being grab from the internet.. Examples: eyes or lips.

```html
<!DOCTYPE html>
<html lang="en">
<head>
<meta charset="utf-8">
<title>Marla Voss – Makeup Artist Business Card</title>
<link rel="stylesheet" href="https://fonts.googleapis.com/css2?family=Sue+Ellen+Francisco&family=Poiret+One&family=Questrial&display=swap">
<style>
  :root {
    --page-bg: #f4f4f4;
    --card-black: #000000;
    --card-glow: #1c1c1c;
    --name-pink: #f3cfd6;
    --name-edge: #b98a93;
    --title-grey: #dcdcdc;
    --contact-white: #e6e6e6;
    --web-pink: #f6d6dd;
    --photo-dark: #2a140b;
    --photo-hair: #6b3a22;
    --photo-warm: #c99a80;
    --photo-light: #ead0c0;
    --shadow: rgba(0, 0, 0, 0.45);
  }
  * { margin: 0; padding: 0; box-sizing: border-box; }
  html, body {
    width: 1200px; height: 1000px; overflow: hidden;
    background: radial-gradient(ellipse at center, #ffffff 0%, var(--page-bg) 70%);
  }
  .card {
    position: absolute; left: 187px; width: 800px; height: 457px;
    border-radius: 10px; overflow: hidden;
    background: var(--card-black);
    box-shadow: 2px 4px 6px var(--shadow);
  }
  .card--front { top: 38px; }
  .card--back {
    top: 518px;
    background: radial-gradient(ellipse 60% 65% at 50% 45%, var(--card-glow) 0%, var(--card-black) 100%);
  }
  .portrait {
    position: absolute; top: 0; right: 0; width: 418px; height: 100%;
    background: linear-gradient(100deg,
      var(--card-black) 0%,
      var(--photo-dark) 14%,
      var(--photo-hair) 36%,
      var(--photo-warm) 62%,
      var(--photo-light) 84%,
      var(--photo-warm) 100%);
  }
  .name {
    position: absolute; left: 14px; top: 34px;
    font-family: "Sue Ellen Francisco", cursive;
    font-weight: 400;
    font-size: 116px; line-height: 1; letter-spacing: 2px;
    color: var(--name-pink);
    text-shadow: 1px 2px 0 var(--name-edge), 2px 4px 4px rgba(0,0,0,0.6);
  }
  .occupation {
    position: absolute; left: 50px; top: 124px;
    font-family: "Poiret One", sans-serif;
    font-size: 50px; line-height: 1; color: var(--title-grey);
  }
  .contact {
    position: absolute; left: 14px; bottom: 10px; list-style: none;
    font-family: "Questrial", sans-serif;
    font-size: 24px; line-height: 29px; color: var(--contact-white);
  }
  .website {
    position: absolute; left: 0; right: 0; top: 198px; text-align: center;
    font-family: "Poiret One", sans-serif;
    font-size: 48px; letter-spacing: 1.5px; color: var(--web-pink);
  }
</style>
</head>
<body>
  <section class="card card--front">
    <div class="portrait" role="img" aria-label="Beauty portrait photograph of a model with long wavy brown hair"></div>
    <h1 class="name">Marla Voss</h1>
    <p class="occupation">Makeup Artist</p>
    <ul class="contact">
      <li>USA: +1 (415)872-6410</li>
      <li>Singapore: +65 83027715</li>
      <li>marlavoss@browsandblush.example</li>
    </ul>
  </section>
  <section class="card card--back">
    <p class="website">www.browsandblush.example</p>
  </section>
</body>
</html>
```